Simple graphic for a book or slide presentation

We are looking for a style that suits the style of our book. It's title is Harbor. Keeping a calm course through stormy seas. There will be more line drawing/graphics in the book but how you design this image will create the style for all the other simple graphics in the book (once we decide what they are). So this one design will lead to a few more to match the style of this one. We'd like the shape of the overall graphic (i.e the arrows and words/bubbles) to be circular (not a rounded square as appears in the sample attached). Perhaps the words don't need to be in ovals or bound by anything at all; perhaps they do - let's see what you see. We'd like you to choose a font or offer many different fonts you think will capture the practical yet unconventional tone of the book. The book is teaching that managing risks in life is a life-skill that can be learned. The section of the book where this graphic will be placed is called "the power of language" - basically we are saying that thoughts, words and actions create our culture and our destiny. This insight comes from Torvel Pelloru's famous quote:
Carefully watch your thoughts, for they become your words.
Manage and watch your words, for they will become your actions.
Consider and judge your actions, for they have become your habits.
Acknowledge and watch your habits, for they shall become your values.
Understand and embrace your values, for they become your destiny.

Please change the text in the middle of the graphic to say: The Human Culture Cycle

```html
<!DOCTYPE html>
<html lang="en">
<head>
<meta charset="utf-8">
<title>The Human Culture Cycle</title>
<link rel="stylesheet" href="https://fonts.googleapis.com/css2?family=Open+Sans:wght@600;700&display=swap">
<style>
  :root {
    --bg: #ffffff;
    --divider: #ffffff;
    --title: #6f6f6f;
    --label: #ffffff;
    --thoughts: #004a87;
    --thoughts-soft: #4a7ea8;
    --words: #1f75bb;
    --words-soft: #5f9bcf;
    --actions: #38a8df;
    --actions-soft: #70c0e8;
    --habits: #00a09a;
    --habits-soft: #4cb9b3;
    --values: #33ab67;
    --values-soft: #6cc28d;
    --culture: #006a35;
    --culture-soft: #4a9069;
  }
  html, body {
    margin: 0;
    padding: 0;
    width: 1200px;
    height: 1000px;
    overflow: hidden;
    background: var(--bg);
  }
  .cycle-diagram {
    display: block;
    width: 1200px;
    height: 1000px;
  }
  .segment {
    stroke: var(--divider);
    stroke-width: 6;
    stroke-linejoin: miter;
  }
  .segment--thoughts { fill: var(--thoughts); }
  .segment--words { fill: var(--words); }
  .segment--actions { fill: var(--actions); }
  .segment--habits { fill: var(--habits); }
  .segment--values { fill: var(--values); }
  .segment--culture { fill: var(--culture); }
  .inner-band .segment--thoughts { fill: var(--thoughts-soft); }
  .inner-band .segment--words { fill: var(--words-soft); }
  .inner-band .segment--actions { fill: var(--actions-soft); }
  .inner-band .segment--habits { fill: var(--habits-soft); }
  .inner-band .segment--values { fill: var(--values-soft); }
  .inner-band .segment--culture { fill: var(--culture-soft); }
  .stage-label {
    font-family: "Open Sans", Arial, sans-serif;
    font-weight: 600;
    font-size: 35px;
    letter-spacing: 2px;
    fill: var(--label);
  }
  .cycle-title {
    font-family: "Open Sans", Arial, sans-serif;
    font-weight: 700;
    font-size: 62px;
    letter-spacing: 3px;
    fill: var(--title);
  }
</style>
</head>
<body>
<svg class="cycle-diagram" viewBox="0 0 1200 1000" role="img" aria-label="The Human Culture Cycle: thoughts, words, actions, habits, values, culture">
  <defs>
    <clipPath id="inner-band-clip">
      <circle cx="600" cy="500" r="285"/>
    </clipPath>
    <path id="label-track" d="M 270 500 A 330 330 0 1 1 930 500 A 330 330 0 1 1 270 500"/>
  </defs>

  <g class="outer-band">
    <path class="segment segment--thoughts" d="M414 177.8 A372 372 0 0 1 786 177.8 L813.5 271.1 L720 292.2 A240 240 0 0 0 480 292.2 L508.5 200.7 Z"/>
    <path class="segment segment--words" d="M786 177.8 A372 372 0 0 1 972 500 L905 570.4 L840 500 A240 240 0 0 0 720 292.2 L813.5 271.1 Z"/>
    <path class="segment segment--actions" d="M972 500 A372 372 0 0 1 786 822.2 L691.5 799.3 L720 707.8 A240 240 0 0 0 840 500 L905 570.4 Z"/>
    <path class="segment segment--habits" d="M786 822.2 A372 372 0 0 1 414 822.2 L386.5 728.9 L480 707.8 A240 240 0 0 0 720 707.8 L691.5 799.3 Z"/>
    <path class="segment segment--values" d="M414 822.2 A372 372 0 0 1 228 500 L295 429.6 L360 500 A240 240 0 0 0 480 707.8 L386.5 728.9 Z"/>
    <path class="segment segment--culture" d="M228 500 A372 372 0 0 1 414 177.8 L508.5 200.7 L480 292.2 A240 240 0 0 0 360 500 L295 429.6 Z"/>
  </g>

  <g class="inner-band" clip-path="url(#inner-band-clip)">
    <path class="segment segment--thoughts" d="M414 177.8 A372 372 0 0 1 786 177.8 L813.5 271.1 L720 292.2 A240 240 0 0 0 480 292.2 L508.5 200.7 Z"/>
    <path class="segment segment--words" d="M786 177.8 A372 372 0 0 1 972 500 L905 570.4 L840 500 A240 240 0 0 0 720 292.2 L813.5 271.1 Z"/>
    <path class="segment segment--actions" d="M972 500 A372 372 0 0 1 786 822.2 L691.5 799.3 L720 707.8 A240 240 0 0 0 840 500 L905 570.4 Z"/>
    <path class="segment segment--habits" d="M786 822.2 A372 372 0 0 1 414 822.2 L386.5 728.9 L480 707.8 A240 240 0 0 0 720 707.8 L691.5 799.3 Z"/>
    <path class="segment segment--values" d="M414 822.2 A372 372 0 0 1 228 500 L295 429.6 L360 500 A240 240 0 0 0 480 707.8 L386.5 728.9 Z"/>
    <path class="segment segment--culture" d="M228 500 A372 372 0 0 1 414 177.8 L508.5 200.7 L480 292.2 A240 240 0 0 0 360 500 L295 429.6 Z"/>
  </g>

  <g class="stage-labels">
    <text class="stage-label"><textPath href="#label-track" startOffset="26.9%" text-anchor="middle">THOUGHTS</textPath></text>
    <text class="stage-label"><textPath href="#label-track" startOffset="44.2%" text-anchor="middle">WORDS</textPath></text>
    <text class="stage-label"><textPath href="#label-track" startOffset="60.6%" text-anchor="middle">ACTIONS</textPath></text>
    <text class="stage-label"><textPath href="#label-track" startOffset="77.5%" text-anchor="middle">HABITS</textPath></text>
    <text class="stage-label"><textPath href="#label-track" startOffset="93.7%" text-anchor="middle">VALUES</textPath></text>
    <text class="stage-label"><textPath href="#label-track" startOffset="10.7%" text-anchor="middle">CULTURE</textPath></text>
  </g>

  <g class="cycle-title" text-anchor="middle">
    <text x="600" y="393">THE</text>
    <text x="600" y="473">HUMAN</text>
    <text x="600" y="553">CULTURE</text>
    <text x="600" y="633">CYCLE</text>
  </g>
</svg>
</body>
</html>
```